Design Large Inspirational Artwork with Long Quote

Design a large piece of art with a quote from Marcus Hallwell.

QUOTE
"The thing that's so interesting about being alive is that you're all in. No matter what you do, you're all in. This is gonna kill you, so I think you might as well play the most magnificent game you can while you're waiting. Because, do you have anything better to do? Why not pick the best thing possible that you could do? Because you're more powerful than you think, way more powerful than you think. I mean, God only knows what you are in the final analysis. You're blind to your own weaknesses, but you're also blind to your own strengths. How far could you take that if you stopped wasting time, and if you stopped lying, and if you oriented yourself to the highest possible good that you could conceive of and you committed to that? How much good could you do? Well, I would say: why don't you find out?"

SIZE
A high-resolution print size of 6' wide and 3' tall should provide ample space for both the quote and the accompanying artwork.

TYPOGRAPHY
Choose a bold, clean, and easily readable font for the quote. You could also experiment with different font sizes for certain words or phrases to emphasize their importance within the quote.

COLORS
Since the quote is thought-provoking and reflective, you might want to use a color palette that evokes a sense of introspection and depth. Consider using cool, calming colors like shades of blue, gray, or green. Alternatively, you can use a contrasting color scheme with a light background and dark text to make the quote stand out.

ARTWORK
Select / create / edit background artwork to complement the quote.
While a great design might be minimalistic and/or greyscale, I'd really like to see some full color options. This might be anything from photography or graphics inspired by the ideas in the text, to abstract colors or illustrations that feel like the sentiment expressed.
The art should capture your attention and encourage you to read the text. The art should be visually appealing, both at a distance and up close, regardless of whether the text is read.
Updates

Having trouble confirming the exact print size.

Still looking for printing solution and final size confirmation.

Target Market(s)

Personal, business, office

Industry/Entity Type

None

Font styles to use
Sans Serif
Script

Requirements
Must have
• Entire quote, legible text, modern design, attractive artwork, approx 6ft wide and 3ft tall
Nice to have
• Different font (sizes) for certain words or phrases to emphasize their importance within the quote.

```html
<!DOCTYPE html>
<html lang="en">
<head>
<meta charset="UTF-8">
<title>All In — Marcus Hallwell Quote Art</title>
<link rel="stylesheet" href="https://fonts.googleapis.com/css2?family=Inter+Tight:wght@400;800&family=Dancing+Script:wght@500&display=swap">
<style>
  :root {
    --backdrop: #558f3e;
    --card-top: #ffffff;
    --card-bottom: #f7f7fc;
    --ink: #1e1e1e;
    --accent: #3e7c1f;
    --mark: #c8c8c8;
    --signature: #7a7a7a;
    --leaf-light: #e9f3e2;
    --leaf-mid: #6ea345;
  }
  * { margin: 0; padding: 0; box-sizing: border-box; }
  html, body {
    width: 1200px;
    height: 804px;
    overflow: hidden;
    background: var(--backdrop);
  }
  .artwork {
    position: absolute;
    left: 110px;
    top: 156px;
    width: 981px;
    height: 491px;
    background: linear-gradient(180deg, var(--card-top) 40%, var(--card-bottom) 100%);
  }
  .leaf-parade {
    position: absolute;
    left: 72px;
    top: 31px;
    width: 828px;
    height: 190px;
    background: linear-gradient(180deg, rgba(255,255,255,0) 0%, var(--leaf-light) 35%, var(--leaf-mid) 80%, var(--leaf-light) 100%);
    border-radius: 6px;
  }
  .quote-mark {
    position: absolute;
    width: 30px;
    height: 32px;
  }
  .quote-mark--open { left: 44px; top: 208px; }
  .quote-mark--close { left: 751px; top: 416px; }
  .quote-mark polygon { fill: var(--mark); }
  .quote-text {
    position: absolute;
    left: 60px;
    top: 233px;
    width: 861px;
    font-family: "Inter Tight", sans-serif;
    font-weight: 400;
    font-size: 17.6px;
    line-height: 25.1px;
    letter-spacing: -0.55px;
    color: var(--ink);
    text-align: center;
  }
  .quote-text strong {
    font-weight: 800;
    color: var(--accent);
    letter-spacing: -0.3px;
  }
  .attribution {
    position: absolute;
    left: 0;
    width: 100%;
    top: 440px;
    font-family: "Dancing Script", cursive;
    font-size: 19px;
    color: var(--signature);
    text-align: center;
  }
</style>
</head>
<body>
  <main class="artwork">
    <div class="leaf-parade" role="img" aria-label="Illustration of a line of leafcutter ants, each carrying a green leaf"></div>

    <svg class="quote-mark quote-mark--open" viewBox="0 0 30 32" aria-hidden="true">
      <polygon points="0,0 11,0 11,12 6,32 0,32"/>
      <polygon points="17,0 29,0 29,12 23,32 17,32"/>
    </svg>

    <p class="quote-text">
      The thing that's so interesting about being alive is that you're <strong>all in.</strong> No matter what you do, you're all in. This is gonna<br>
      kill you, so I think you might as well play the most magnificent game you can while you're waiting. Because, do you<br>
      have anything better to do? Why not pick the <strong>best thing possible</strong> that you could do? Because you're more powerful<br>
      than you think, way <strong>more powerful than you think.</strong><br>
      I mean, God only knows what you are in the final analysis. You're <strong>blind to your own weaknesses,</strong> but you're also<br>
      <strong>blind to your own strengths.</strong> How far could you take that if you stopped wasting time, and if you stopped lying, and<br>
      if you oriented yourself to the <strong>highest possible good</strong> that you could conceive of and you committed to that? How<br>
      much good could you do? Well, I would say: why don't you find out?
    </p>

    <svg class="quote-mark quote-mark--close" viewBox="0 0 30 32" aria-hidden="true">
      <polygon points="0,0 11,0 11,12 6,32 0,32"/>
      <polygon points="17,0 29,0 29,12 23,32 17,32"/>
    </svg>

    <p class="attribution">- Marcus Hallwell -</p>
  </main>
</body>
</html>
```